Residential Roofing Company

Website for Residential roofing company. Servicing Minnesota (Hennepin, Anoka, Sherburne County). Located in Ramsey, Minnesota. Asphalt Shingles (TLR and Palder Brisk Manufacturers)

Target Market(s)

Storm Damage repair. Roof Replacement and Repair.

Industry/Entity Type

Residential Roofing

Coding

Coded - Design and coding required

Number of Pages Required

5+ page

Colors

Designer to choose colors to be used in the design.

Requirements
Should not have
• No Commercial Roofing

```html
<!DOCTYPE html>
<html lang="en">
<head>
<meta charset="utf-8">
<title>Halden Roofing – Mobile Screens</title>
<link href="https://fonts.googleapis.com/css2?family=Poppins:wght@400;500;600;700&display=swap" rel="stylesheet">
<style>
:root{
  --blue:#0b3ea6;
  --cyan:#1ec8f5;
  --ink:#141414;
  --text:#555;
  --light:#efefef;
  --dark:#262628;
  --black:#050505;
  --star:#f5c518;
  --white:#fff;
  --grad:linear-gradient(90deg,var(--blue),var(--cyan));
}
*{box-sizing:border-box;margin:0;padding:0}
html,body{width:891px;height:1200px;overflow:hidden;background:var(--white)}
body{position:relative;font-family:'Poppins',sans-serif;color:var(--ink)}
.screen{position:absolute;width:166px;overflow:hidden}
.center{text-align:center}
.title{font-weight:600;font-size:12px;line-height:1.45;text-transform:uppercase;letter-spacing:.3px}
.title strong{font-weight:700}
.bar{display:block;width:64px;height:2px;margin:5px auto 7px;background:var(--grad);border-radius:2px}
.body-text{font-size:5.6px;line-height:1.6;color:var(--text)}
.btn{display:inline-block;background:var(--grad);color:var(--white);font-size:6px;font-weight:500;padding:5px 9px;text-transform:uppercase;letter-spacing:.3px}
.btn-dark{background:#4a4a4a}
.logo{font-weight:700;color:var(--blue);letter-spacing:1px;text-transform:uppercase}
.photo{display:block}

/* Hero */
.hero{left:24px;top:34px;height:289px;background:#3c3e42}
.hero-header{height:32px;background:var(--white);display:flex;align-items:center;justify-content:space-between;padding:0 8px}
.hero-header .logo{font-size:11px}
.menu-icon span{display:block;width:12px;height:1.5px;background:#222;margin:2.5px 0}
.hero-photo{position:absolute;left:0;top:32px;width:166px;height:257px;background:linear-gradient(160deg,#6a6d72 0%,#4b4d52 45%,#2f3033 100%)}
.hero-copy{position:absolute;left:0;right:0;top:150px;text-align:center;color:var(--white)}
.hero-copy h1{font-size:18.5px;font-weight:400;line-height:1.22;letter-spacing:.3px}
.hero-copy h1 strong{font-weight:700}
.hero-copy p{font-size:6px;line-height:1.6;margin:8px 14px 9px}

/* Services */
.services{left:24px;top:337px;height:660px}
.services .title{font-size:12.5px;font-weight:400}
.services .body-text{padding:0 10px}
.hex-field{position:absolute;left:0;top:80px}

/* About */
.about{left:236px;top:44px;height:394px;background:var(--light);padding:26px 8px 0}
.about .body-text{padding:0 6px}
.about-gallery{position:relative;height:122px;margin:10px 0 8px}
.about-main{position:absolute;left:22px;top:0;width:122px;height:100px;background:linear-gradient(180deg,#b9c3cf 0%,#8a8f96 45%,#3e3a36 100%);border:2px solid var(--white)}
.about-inset{position:absolute;left:0;top:70px;width:62px;height:46px;background:linear-gradient(160deg,#c7b79e,#6f6a62);border:2px solid var(--white)}
.about-lead{font-size:5.8px;font-weight:600;line-height:1.55;color:var(--ink);margin-bottom:6px}
.about .btn{margin-top:12px}

/* Stats */
.stats{left:236px;top:438px;height:124px;background:var(--black);color:var(--white)}
.stat{position:absolute;display:flex;align-items:center;gap:6px}
.stat-icon{width:24px;height:22px;background:var(--blue);border-radius:3px}
.stat b{display:block;font-size:15px;font-weight:500;line-height:1}
.stat small{display:block;font-size:4px;color:#bbb;margin-top:2px}
.stat-divider{position:absolute;left:50px;top:112px;width:130px;height:1px;background:#aaa;transform:rotate(-47deg);transform-origin:left}

/* Service levels */
.levels{left:236px;top:562px;height:489px;background:linear-gradient(180deg,#3a3a3c 0%,#2f2e2f 45%,#5a3826 80%,#3e2515 100%);color:var(--white);padding:24px 10px 0}
.levels .title{font-size:11.5px;letter-spacing:.6px}
.levels .bar{background:#ddd;width:56px}
.level{margin-top:14px}
.level svg{display:block;margin:0 auto 6px}
.level h3{font-size:6.2px;font-weight:600}
.level .dash{display:block;width:8px;height:1px;background:#fff;margin:4px auto}
.level p{font-size:5.6px;line-height:1.65;color:#ddd;padding:0 8px}
.diamond{display:block;width:5px;height:5px;background:var(--cyan);transform:rotate(45deg);margin:10px auto 0}

/* Testimonials */
.topline{left:428px;top:34px;height:4px;background:#3b2a1e}
.reviews{left:428px;top:38px;height:608px;background:var(--white);padding:22px 4px 0}
.rating{font-size:5px;color:var(--text);margin-top:-1px;line-height:1.5}
.rating .stars{color:var(--star)}
.rating b{color:var(--blue)}
.review{position:relative;margin:12px 6px 0;height:158px}
.review-card{height:108px;background:var(--white);box-shadow:0 2px 8px rgba(0,0,0,.16);padding:6px 14px 0 22px}
.quote{font-size:20px;font-weight:700;color:#444;line-height:.9;margin-left:-2px}
.review-card p{font-size:5.4px;line-height:1.65;color:var(--text);font-style:italic;margin-top:3px}
.avatar{position:absolute;left:63px;top:88px;width:32px;height:32px;border-radius:50%;border:2px solid var(--blue);background:linear-gradient(160deg,#8d7a6b,#4a3f3a)}
.reviewer{position:absolute;left:0;right:0;top:124px;text-align:center;font-size:6px;font-weight:600}
.reviewer .stars{display:block;color:var(--star);font-size:7px;letter-spacing:1.5px;margin-top:2px}
.dots{display:flex;gap:4px;justify-content:center;margin-top:4px}
.dots i{width:4px;height:4px;border-radius:50%;background:#ccc}
.dots i.on{background:var(--blue)}

/* Projects */
.projects{left:428px;top:646px;height:174px;background:linear-gradient(180deg,#dcdcdc,#bfbfbf);padding:24px 0 0}
.projects .title{font-size:11.5px}
.project-card{position:relative;width:122px;height:74px;margin:2px auto 0;background:linear-gradient(180deg,#8fb2d4 0%,#c7c3bb 55%,#5a6a4a 100%);border:2px solid var(--white)}
.project-caption{position:absolute;left:0;right:0;bottom:0;background:rgba(0,0,0,.7);color:var(--white);padding:3px 5px;font-size:3.6px;line-height:1.5}
.project-caption b{display:block;font-size:4.2px}

/* Areas */
.areas{left:428px;top:820px;height:259px;background:var(--light);padding:24px 8px 0}
.areas .title{font-size:11.5px}
.map{position:relative;height:120px;margin:10px -4px 0;background:linear-gradient(160deg,#a9c4f5,#7fa6ee)}
.map-label{position:absolute;left:10px;top:84px;background:var(--white);padding:3px 5px;font-size:3.6px;color:var(--text);line-height:1.5}
.map-label b{display:block;color:var(--ink);font-size:4px}

/* CTA */
.cta{left:620px;top:124px;height:169px;background:var(--light);padding:24px 0 0}
.cta .logo{font-size:10px}
.cta h2{font-size:11.5px;font-weight:400;letter-spacing:.5px;margin-top:10px;line-height:1.5}
.cta h2 strong{font-weight:700;display:block}
.cta .btn{width:92px;text-align:center;margin-top:3px}

/* Contact */
.contact{left:620px;top:293px;height:247px;background:linear-gradient(180deg,#2f2f31,#1e1e20);color:var(--white);padding:20px 6px 0}
.eyebrow{font-size:5px;color:#ccc;letter-spacing:.6px;text-transform:uppercase}
.contact .title{font-size:11px;font-weight:400;letter-spacing:.6px}
.contact .bar{background:#ddd}
.field{background:var(--white);height:16px;margin-bottom:8px;font-size:4.8px;color:#888;padding:5px 4px}
.field.area{height:48px}
.contact .btn{margin-top:0}

/* Footer */
.footer{left:620px;top:540px;height:392px;background:var(--black);color:var(--white);padding:24px 8px 0}
.footer .logo{font-size:14px;color:var(--cyan)}
.footer-about{font-size:4.2px;color:#bbb;line-height:1.6;margin:6px 18px 0}
.social{display:flex;gap:5px;justify-content:center;margin-top:10px}
.social i{width:10px;height:10px;border-radius:50%;background:var(--white)}
.link-cols{display:flex;justify-content:space-between;margin-top:18px}
.footer h4{font-size:6.2px;font-weight:600;margin-bottom:8px;line-height:1.3}
.footer ul{list-style:none}
.footer li{font-size:5px;line-height:1.3;color:#ddd;margin-bottom:9px}
.footer li::before{content:"▸";font-size:4px;margin-right:5px}
.contact-info{margin-top:12px}
.info-row{display:flex;gap:8px;align-items:flex-start;margin-bottom:10px}
.info-icon{flex:none;width:14px;height:14px;border-radius:50%;background:var(--grad);display:flex;align-items:center;justify-content:center}
.info-text{font-size:0;line-height:1}
.info-text b{display:block;font-size:5px;font-weight:600;line-height:1.4;margin-bottom:2px}
.info-text span{display:block;font-size:4.2px;color:#ccc;line-height:1.5}
.legal{border-top:1px solid #333;margin-top:12px;padding-top:7px;font-size:4.2px;color:#ccc;line-height:2.4}
.legal em{font-style:normal;color:var(--cyan)}
</style>
</head>
<body>

<!-- Hero -->
<section class="screen hero">
  <header class="hero-header">
    <span class="logo">Halden Roofing</span>
    <span class="menu-icon"><span></span><span></span><span></span></span>
  </header>
  <div class="hero-photo photo" role="img" aria-label="Roofer in a hard hat working on a roof"></div>
  <div class="hero-copy">
    <h1><strong>LEADERS</strong> IN<br>QUALITY<br>ROOFING</h1>
    <p>We've roofers delivering superior quality roof repair &amp; replacement</p>
    <span class="btn">Get a Free Estimate</span>
  </div>
</section>

<!-- Services -->
<section class="screen services center">
  <h2 class="title"><strong>OUR</strong> SERVICES</h2>
  <span class="bar"></span>
  <p class="body-text">Lorem ipsum dolor sit amet, consectetur adipiscing elit. Diam consequat massa morbi aliquet purus tincidunt et venenatis id.</p>
  <svg class="hex-field" width="166" height="580" viewBox="0 0 166 580" aria-label="Service list">
    <defs>
      <linearGradient id="hexDark" x1="0" y1="0" x2="0" y2="1"><stop offset="0" stop-color="#5a5b5f"/><stop offset="1" stop-color="#2c2d30"/></linearGradient>
      <linearGradient id="hexBlue" x1="0" y1="0" x2="1" y2="1"><stop offset="0" stop-color="#1ec8f5"/><stop offset="1" stop-color="#0b3ea6"/></linearGradient>
      <polygon id="outer" points="0,-62 53.7,-31 53.7,31 0,62 -53.7,31 -53.7,-31"/>
      <polygon id="inner" points="0,-52 45,-26 45,26 0,52 -45,26 -45,-26"/>
      <polygon id="badge" points="0,-17 14.7,-8.5 14.7,8.5 0,17 -14.7,8.5 -14.7,-8.5"/>
    </defs>
    <g font-family="Poppins, sans-serif" font-size="8.5" font-weight="500" fill="#fff" text-anchor="middle" letter-spacing=".4">
      <g transform="translate(62,62)">
        <use href="#outer" fill="#fff" stroke="#e6e6e6"/><use href="#inner" fill="url(#hexDark)"/>
        <use href="#badge" y="-18" fill="url(#hexBlue)"/>
        <path d="M-6,-17 L0,-23 L6,-17 L6,-12 L-6,-12Z" fill="#fff"/>
        <text y="12">RESIDENTIAL</text><text y="23">ROOFING</text>
      </g>
      <g transform="translate(108,172)">
        <use href="#outer" fill="#fff" stroke="#e6e6e6"/><use href="#inner" fill="url(#hexBlue)"/>
        <rect x="-12" y="-32" width="24" height="24" rx="4" fill="#fff"/>
        <path d="M-6,-24 H6 V-15 H-6Z" fill="#0b3ea6"/>
        <text y="14">FLAT ROOF</text>
      </g>
      <g transform="translate(62,282)">
        <use href="#outer" fill="#fff" stroke="#e6e6e6"/><use href="#inner" fill="url(#hexDark)"/>
        <use href="#badge" y="-18" fill="url(#hexBlue)"/>
        <path d="M-6,-22 H6 V-13 H-6Z" fill="none" stroke="#fff" stroke-width="1.2"/>
        <text y="18">INSULATION</text>
      </g>
      <g transform="translate(108,392)">
        <use href="#outer" fill="#fff" stroke="#e6e6e6"/><use href="#inner" fill="url(#hexDark)"/>
        <use href="#badge" y="-18" fill="url(#hexBlue)"/>
        <text y="12">INSURANCE</text><text y="23">CLAIMS</text>
      </g>
      <g transform="translate(62,502)">
        <use href="#outer" fill="#fff" stroke="#e6e6e6"/><use href="#inner" fill="url(#hexDark)"/>
        <use href="#badge" y="-18" fill="url(#hexBlue)"/>
        <path d="M-6,-17 L0,-23 L6,-17 L6,-12 L-6,-12Z" fill="#fff"/>
        <text y="12">SIDING /</text><text y="23">WINDOWS</text>
      </g>
    </g>
  </svg>
</section>

<!-- About -->
<section class="screen about">
  <h2 class="title center">About Halden<br>Roofing</h2>
  <span class="bar"></span>
  <p class="body-text center">Lorem ipsum dolor sit amet, consectetur adipiscing elit. Diam consequat massa morbi aliquet purus tincidunt et venenatis id.</p>
  <div class="about-gallery">
    <div class="about-main photo" role="img" aria-label="House with a new dark metal roof"></div>
    <div class="about-inset photo" role="img" aria-label="Roofer installing shingles"></div>
  </div>
  <p class="about-lead">With over 40 years of experience in servicing the residents of the Twin Cities area, the Halden Roofing team knows what it takes to get the job done right!</p>
  <p class="body-text">We are a second generation roofing company that has instilled a modern touch into our brand. Halden Roofing is a Woman Owned and Operated Company. We've implemented the knowledge and successful business practices from our history and experience into our brand. Roofing is our history and we strive to make sure our customers receive the best experience possible.</p>
  <div class="center"><span class="btn">Read More →</span></div>
</section>

<!-- Stats -->
<section class="screen stats">
  <div class="stat" style="left:12px;top:24px"><span class="stat-icon"></span><span><b>1987</b><small>Years Established</small></span></div>
  <span class="stat-divider"></span>
  <div class="stat" style="left:84px;top:78px"><span class="stat-icon"></span><span><b>1000'S</b><small>Satisfied Customers</small></span></div>
</section>

<!-- Service levels -->
<section class="screen levels center" role="group" aria-label="House exterior backdrop">
  <h2 class="title">We Provide<br>The Highest Level<br>Of Service</h2>
  <span class="bar"></span>
  <div class="level">
    <svg width="32" height="34" viewBox="0 0 32 34"><rect x="2" y="2" width="20" height="28" rx="3" fill="none" stroke="#fff" stroke-width="1.5"/><rect x="6" y="6" width="12" height="6" fill="#fff"/><circle cx="24" cy="26" r="7" fill="#1ec8f5"/></svg>
    <h3>Free Assessments Estimates</h3><span class="dash"></span>
    <p>Roofing is our history and we strive to make sure our customers receive the best experience possible.</p>
    <span class="diamond"></span>
  </div>
  <div class="level">
    <svg width="32" height="34" viewBox="0 0 32 34"><path d="M16 2 L28 7 V16 C28 24 22 29 16 32 C10 29 4 24 4 16 V7Z" fill="none" stroke="#fff" stroke-width="1.5"/><path d="M16 8 L23 11 V17 C23 22 19 25 16 27 C13 25 9 22 9 17 V11Z" fill="#1ec8f5"/><path d="M12 17 L15 20 L20 14" stroke="#fff" stroke-width="1.5" fill="none"/></svg>
    <h3>All Work Warrantied</h3><span class="dash"></span>
    <p>Roofing is our history and we strive to make sure our customers receive the best experience possible.</p>
    <span class="diamond"></span>
  </div>
  <div class="level">
    <svg width="32" height="34" viewBox="0 0 32 34"><path d="M6 2 H20 L26 8 V32 H6Z" fill="none" stroke="#fff" stroke-width="1.5"/><path d="M10 12 H20 M10 16 H20" stroke="#fff"/><circle cx="20" cy="25" r="4" fill="#1ec8f5"/></svg>
    <h3>Licensed, Bounded &amp;<br>Insured</h3><span class="dash"></span>
    <p>Roofing is our history and we strive to make sure our customers receive the best experience possible.</p>
  </div>
</section>

<!-- Testimonials -->
<div class="screen topline"></div>
<section class="screen reviews center">
  <h2 class="title">What Our<br>Customers Say's</h2>
  <span class="bar"></span>
  <p class="rating"><span class="stars">★★★★★</span> rated <b>4.9</b> out of <b>5</b> based on <b>564 reviews</b><br>from around the web</p>
  <div class="review">
    <div class="review-card" style="text-align:left"><div class="quote">❝</div><p>Lorem ipsum dolor sit amet, consectetur adipiscing elit. Diam consequat massa morbi aliquet purus tincidunt et venenatis id. Nec enim ipsum sed leo sed. Ut interdum bibendum condimentum justo, augue.</p></div>
    <div class="avatar" role="img" aria-label="Customer portrait"></div>
    <div class="reviewer">Marcus Hale<span class="stars">★★★★★</span></div>
  </div>
  <div class="review">
    <div class="review-card" style="text-align:left"><div class="quote">❝</div><p>Lorem ipsum dolor sit amet, consectetur adipiscing elit. Diam consequat massa morbi aliquet purus tincidunt et venenatis id. Nec enim ipsum sed leo sed. Ut interdum bibendum condimentum justo, augue.</p></div>
    <div class="avatar" role="img" aria-label="Customer portrait"></div>
    <div class="reviewer">Priya Okafor<span class="stars">★★★★★</span></div>
  </div>
  <div class="review">
    <div class="review-card" style="text-align:left"><div class="quote">❝</div><p>Lorem ipsum dolor sit amet, consectetur adipiscing elit. Diam consequat massa morbi aliquet purus tincidunt et venenatis id. Nec enim ipsum sed leo sed. Ut interdum bibendum condimentum justo, augue.</p></div>
    <div class="avatar" role="img" aria-label="Customer portrait"></div>
    <div class="reviewer">Lena Ostrow<span class="stars">★★★★★</span></div>
  </div>
  <div class="dots"><i></i><i class="on"></i><i></i><i></i></div>
</section>

<!-- Projects -->
<section class="screen projects center" role="group" aria-label="Roof framing backdrop">
  <h2 class="title">View Our Resent<br>Progects Below</h2>
  <span class="bar"></span>
  <div class="project-card photo" role="img" aria-label="Two-storey family home with a finished roof">
    <div class="project-caption" style="text-align:left"><b>Lorem Project Name</b>Lorem ipsum dolor sit amet, consectetur adipiscing elit. Diam consequat massa morbi aliquet purus tincidunt et venenatis id.</div>
  </div>
</section>

<!-- Areas -->
<section class="screen areas center">
  <h2 class="title">Areas We Serve</h2>
  <span class="bar"></span>
  <p class="body-text">Lorem ipsum dolor sit amet, consectetur adipiscing elit. Diam consequat massa morbi aliquet purus tincidunt et venenatis id. Nec enim ipsum sed leo sed. Ut interdum bibendum condimentum justo, egestas augue.</p>
  <div class="map" role="img" aria-label="Map of Minnesota counties with service location pins">
    <div class="map-label" style="text-align:left"><b>Location Name</b>Lorem ipsum dolor sit<br>amet consectetur</div>
  </div>
</section>

<!-- CTA -->
<section class="screen cta center">
  <span class="logo">Halden Roofing</span>
  <h2>READY TOSCHEDULE<strong>FREE ESTIMATE?</strong></h2>
  <span class="bar"></span>
  <span class="btn">Get a Free Estimate</span><br>
  <span class="btn btn-dark" style="margin-top:9px">Contact Us Today</span>
</section>

<!-- Contact -->
<section class="screen contact">
  <div class="center">
    <p class="eyebrow">Contact Us</p>
    <h2 class="title" style="margin-top:5px">Reliable &amp; Trusted<br><strong>Roofing Services</strong></h2>
    <span class="bar"></span>
  </div>
  <div class="field">Name *</div>
  <div class="field">Phone *</div>
  <div class="field">Email *</div>
  <div class="field area">Write Message here</div>
  <div class="center"><span class="btn">Submit Now</span></div>
</section>

<!-- Footer -->
<footer class="screen footer">
  <div class="center">
    <span class="logo">Halden Roofing</span>
    <p class="footer-about">Lorem ipsum dolor sit amet, consectetur adipiscing elit pharetra faucibus fames</p>
    <div class="social"><i></i><i></i><i></i><i></i></div>
  </div>
  <div class="link-cols">
    <div>
      <h4>Quick Links</h4>
      <ul><li>Home</li><li>About Us</li><li>Services</li><li>Projects</li><li>Contact Us</li></ul>
    </div>
    <div style="width:82px">
      <h4>Customer Services</h4>
      <ul><li>Residential Roofing</li><li>Flat Roof</li><li>Siding / Windows</li></ul>
    </div>
  </div>
  <div class="contact-info">
    <h4>Our Contact Info</h4>
    <div class="info-row">
      <span class="info-icon"><svg width="7" height="8" viewBox="0 0 7 8"><path d="M3.5 0 A3 3 0 0 1 6.5 3 C6.5 5 3.5 8 3.5 8 C3.5 8 0.5 5 0.5 3 A3 3 0 0 1 3.5 0Z" fill="#fff"/><circle cx="3.5" cy="3" r="1.1" fill="#0b3ea6"/></svg></span>
      <div class="info-text"><b>Location</b><span>1840 Birchwood Ave. Ramsey,</span><span>MN 55303</span></div>
    </div>
    <div class="info-row">
      <span class="info-icon"><svg width="7" height="7" viewBox="0 0 7 7"><path d="M1 0.5 L2.6 0.5 L3 2.2 L2 3 C2.5 4 3 4.5 4 5 L4.8 4 L6.5 4.4 L6.5 6 C3 6.3 0.7 4 1 0.5Z" fill="#fff"/></svg></span>
      <div class="info-text"><b>Phone</b><span>763-555-0142</span></div>
    </div>
    <div class="info-row">
      <span class="info-icon"><svg width="7" height="6" viewBox="0 0 7 6"><rect x="0.5" y="0.5" width="6" height="5" fill="#fff"/><path d="M0.5 0.5 L3.5 3 L6.5 0.5" stroke="#0b3ea6" stroke-width=".7" fill="none"/></svg></span>
      <div class="info-text"><b>Mail</b><span>hello@haldenroofing.example</span></div>
    </div>
  </div>
  <div class="legal center">Privacy Policy &nbsp;|&nbsp; Terms and Conditions<br>©Copyright 2022, <em>HALDEN ROOFING</em> | All Rights Reserved</div>
</footer>

</body>
</html>
```